I need a business card design for a new dance business. I offer classical Indian dance tuition and also professional performances. I want to offer the community a variety of Indian dance experiences which include: group class and private tuition, school and preschool educational courses and workshops. dance theatre performances, community function workshops and performances, Kids Bollywood parties, wedding & conference performances, mouth percussion classes, Indian mythology/ dance costume and make up workshops.
The final design should communicate a feeling and impression of the vibrance and energy of Indian dance.
Updates
Hi Everyone,
Project Deadline Extended
Reason: I would like to refine a few changes to the details of this lovely design and we have run out of time!
Project Deadline Extended
Reason: Still waiting to hear back form designer re two possible changes to the card design. Tomorrow is the deadline and I have sent several messages but with no response. I need to see this through before selecting this lovely design.
Thank you.
Tessa
Industry/Entity Type
Preschool
Requirements
Must have
- The front of the business card should have the photo of me (my face and torso), surrounded entirely by a border of bright magenta (to match the magenta of my lipstick - it is the same as the magenta on my skirt in the second photo). Within the top border I want (perhaps yellow-gold) writing to say "Tessa Marlowe - Artistic Director" and within the bottom border it should read "Copper Lantern Indian Dance." If you turn the card on its side the left border should have my telephone number: 0417 862 049 and the right-hand border should read: copperlanternindiandance@velmora.com
The reverse of the card should be the orange of the dance costume
and I'd like the picture of my feet and legs to be on the right side of the back of the card as a side border. Centre-aligned on the orange background it should read (perhaps in dark magenta):
Indian dance classes + private tuition
School + preschool educational courses and workshops
Dance theatre performances
Community function workshops and performances
Children's Bollywood parties
Wedding + conference performances
Mouth percussion classes
Indian mythology and dance demonstration workshops
Dance costume and make-up workshops
Nice to have
- A lovely artistic but easy-to-read font would be nice.

```html
<!DOCTYPE html>
<html lang="en">
<head>
<meta charset="utf-8">
<title>Copper Lantern Indian Dance – Business Cards</title>
<link rel="stylesheet" href="https://fonts.googleapis.com/css2?family=Kaushan+Script&display=swap">
<style>
  :root {
    --page: #ffffff;
    --magenta: #b900cf;
    --orange: #f39300;
    --cream: #fbfbeb;
    --gold: #f6b631;
    --amber: #f09a1c;
    --plum: #a8118f;
    --skin-light: #efc7b3;
    --costume: #e98a1e;
    --silk: #c32fb8;
  }
  html, body {
    margin: 0;
    width: 1200px;
    height: 342px;
    overflow: hidden;
    background: var(--page);
  }
  .sheet {
    position: relative;
    width: 1200px;
    height: 342px;
    font-family: "Kaushan Script", cursive;
  }
  .card {
    position: absolute;
    top: 109px;
    width: 371px;
    height: 212px;
    overflow: hidden;
  }
  .card--front-magenta { left: 18px; background: var(--magenta); }
  .card--back { left: 418px; background: var(--orange); }
  .card--front-cream { left: 818px; background: var(--cream); }

  .brand {
    position: absolute;
    top: 8px;
    right: 14px;
    margin: 0;
    font-size: 14px;
    font-weight: 400;
    color: var(--gold);
    z-index: 2;
  }
  .card--front-cream .brand { color: var(--amber); }

  .identity {
    position: absolute;
    left: 10px;
    top: 34px;
    z-index: 2;
  }
  .identity__name {
    margin: 0;
    font-size: 12px;
    color: var(--gold);
  }
  .identity__role {
    margin: 1px 0 0;
    font-size: 8.5px;
    color: var(--gold);
  }
  .card--front-cream .identity__name,
  .card--front-cream .identity__role,
  .card--front-cream .contact { color: var(--amber); }

  .contact {
    position: absolute;
    left: 10px;
    bottom: 8px;
    margin: 0;
    font-size: 9.5px;
    line-height: 20px;
    color: var(--gold);
    z-index: 2;
  }

  .portrait {
    position: absolute;
    left: 168px;
    top: 38px;
    width: 196px;
    height: 174px;
    border-radius: 90px 90px 0 0;
    background: radial-gradient(ellipse at 50% 35%, var(--skin-light) 0%, var(--skin-light) 22%, var(--costume) 55%, rgba(233,138,30,0) 75%);
  }

  .services {
    position: absolute;
    left: 7px;
    top: 26px;
    margin: 0;
    padding: 0;
    list-style: none;
    font-size: 9px;
    line-height: 19px;
    color: var(--plum);
  }
  .dancer-legs {
    position: absolute;
    left: 248px;
    top: 0;
    width: 112px;
    height: 212px;
    background: linear-gradient(180deg, var(--silk) 0%, var(--silk) 45%, var(--costume) 70%, var(--skin-light) 100%);
    border-radius: 30px 30px 10px 10px;
  }
</style>
</head>
<body>
<div class="sheet">

  <section class="card card--front-magenta">
    <h1 class="brand">Copper Lantern Indian Dance</h1>
    <div class="identity">
      <p class="identity__name">Tessa Marlowe</p>
      <p class="identity__role">Graduate of Kuchipudi classical Indian dance</p>
    </div>
    <div class="portrait" role="img" aria-label="Photo of the dancer in costume and jewellery, hands raised beside her head"></div>
    <p class="contact">Ph: 0417 862 049<br>copperlanternindiandance@velmora.com</p>
  </section>

  <section class="card card--back">
    <ul class="services">
      <li>Indian dance classes + private tuition</li>
      <li>Dance theatre performances</li>
      <li>Children's parties</li>
      <li>Wedding + conference performances</li>
      <li>Mouth percussion classes</li>
      <li>Community function workshops and performances</li>
      <li>School + preschool educational courses and workshops</li>
      <li>Indian mythology and dance demonstration workshops</li>
    </ul>
    <div class="dancer-legs" role="img" aria-label="Photo of the dancer's legs and feet in a magenta and orange costume"></div>
  </section>

  <section class="card card--front-cream">
    <h1 class="brand">Copper Lantern Indian Dance</h1>
    <div class="identity">
      <p class="identity__name">Tessa Marlowe</p>
      <p class="identity__role">Graduate of Kuchipudi classical Indian dance</p>
    </div>
    <div class="portrait" role="img" aria-label="Photo of the dancer in costume and jewellery, hands raised beside her head"></div>
    <p class="contact">Ph: 0417 862 049<br>copperlanternindiandance@velmora.com</p>
  </section>

</div>
</body>
</html>
```